All Out No Regrets Art

I'd like my motto "All Out No Regrets" made into art for my office. I'm in a very formal/conservative office building but my office is more modern and upbeat. Even though the motto sounds really bold and maybe even harsh, I'm looking for something upbeat and happy. Nothing too harsh/angular, I like swirls and modern whimsical things. Love the colors orange, gray and bright/lime green but it doesn't have to be just those colors or all those colors. I do NOT like navy blue and burgandy.
This needs to look like high-quality art, not like a "poster" because it's for an executive office.
I've updated the creative brief.

```html
<!DOCTYPE html>
<html lang="en">
<head>
<meta charset="utf-8">
<title>All Out No Regrets</title>
<link rel="stylesheet" href="https://fonts.googleapis.com/css2?family=Roboto:wght@100;400;700&display=swap">
<style>
  :root {
    --frame-gray: #8f9092;
    --panel-orange: #f7a800;
    --panel-yellow: #fbbd14;
    --swirl-light: #fcd24a;
    --text-white: #ffffff;
    --lime: #9ccc3c;
  }
  * { margin: 0; padding: 0; box-sizing: border-box; }
  html, body {
    width: 857px;
    height: 1200px;
    overflow: hidden;
    background: var(--frame-gray);
  }
  .artwork {
    position: relative;
    width: 857px;
    height: 1200px;
    background: var(--frame-gray);
  }
  .artwork__panel {
    position: absolute;
    left: 40px;
    top: 46px;
    width: 783px;
    height: 1108px;
    background:
      radial-gradient(circle at 70% 30%, var(--swirl-light) 0%, transparent 45%),
      radial-gradient(circle at 25% 80%, var(--swirl-light) 0%, transparent 40%),
      linear-gradient(160deg, var(--panel-yellow) 0%, var(--panel-orange) 100%);
  }
  .motto {
    position: absolute;
    left: 466px;
    top: 270px;
    transform: translateX(-50%);
    display: flex;
    flex-direction: column;
    align-items: center;
    font-family: "Roboto", Arial, sans-serif;
    line-height: 0.8;
    text-align: center;
  }
  .motto__word { display: block; }
  .motto__all {
    font-weight: 700;
    font-size: 200px;
    color: var(--text-white);
    letter-spacing: -4px;
  }
  .motto__out {
    font-weight: 100;
    font-size: 214px;
    color: transparent;
    -webkit-text-stroke: 2px var(--text-white);
    margin-top: 16px;
  }
  .motto__no {
    font-weight: 400;
    font-size: 200px;
    color: var(--lime);
    margin-top: 22px;
  }
  .motto__regrets {
    font-weight: 700;
    font-size: 70px;
    color: var(--text-white);
    margin-top: 18px;
  }
</style>
</head>
<body>
  <main class="artwork">
    <div class="artwork__panel" role="img" aria-label="Warm orange and yellow background with flowing light swirls, curling vines, small flowers and butterflies"></div>
    <h1 class="motto">
      <span class="motto__word motto__all">ALL</span>
      <span class="motto__word motto__out">OUT</span>
      <span class="motto__word motto__no">NO</span>
      <span class="motto__word motto__regrets">REGRETS</span>
    </h1>
  </main>
</body>
</html>
```